Medical device company presentation

Traloma is an early stage medical device company. We are developing an Ultrasound based catheter to treat hypertension.
We'd like the presentation slides to be clean with green/blue colors (Attached is our Logo which should part of each slide).
Updates
Project Deadline Extended
Reason: I would like to receive more designs options.
I received only 3-4 good and full designs.
Target Market(s)
Medical device companies
Industry/Entity Type
It Company
Look and feel

```html
<!DOCTYPE html>
<html lang="en">
<head>
<meta charset="utf-8">
<title>Traloma slide template overview</title>
<link href="https://fonts.googleapis.com/css2?family=Open+Sans:wght@400;600;700&display=swap" rel="stylesheet">
<style>
:root{
  --bg:#e5e5e5;
  --blue:#2d8be3;
  --blue-dark:#1f76cc;
  --green:#7cc143;
  --grey:#cccccc;
  --grey-dark:#b9b9b9;
  --text:#555;
  --white:#fff;
}
*{box-sizing:border-box;margin:0;padding:0}
html,body{width:1200px;height:1200px;overflow:hidden;background:var(--bg);font-family:"Open Sans",Arial,sans-serif}
.slide{position:absolute;width:282px;height:158px;background:var(--white);box-shadow:1px 1px 3px rgba(0,0,0,.3);overflow:hidden}
.c1{left:22px}.c2{left:318px}.c3{left:614px}.c4{left:910px}
.r1{top:25px}.r2{top:228px}.r3{top:432px}.r4{top:635px}.r5{top:838px}.r6{top:1018px}
.abs{position:absolute}
.hd{position:absolute;left:11px;top:20px;font-size:9px;font-weight:700;color:var(--blue);letter-spacing:.6px}
.brand{position:absolute;right:10px;top:10px;font-size:11px;color:var(--green);font-weight:400}
.rule{position:absolute;left:0;right:0;top:33px;height:3px;border-top:1.5px solid var(--blue);border-bottom:1.5px solid var(--green)}
.tx{font-size:3.6px;line-height:1.45;color:var(--text)}
.tx.w{color:var(--white)}
.ph{position:absolute;background:var(--grey)}
.ph::after{content:"";position:absolute;left:50%;top:50%;width:16%;max-width:20px;aspect-ratio:1.1;transform:translate(-50%,-50%);border:2px solid var(--white);border-radius:1px}
.bar{position:absolute;background:var(--blue);color:var(--white);font-size:4.5px;font-weight:700;text-align:center;letter-spacing:.4px}
.box{position:absolute;border:1px solid var(--blue);padding:3px}
ul.tx{list-style:none}
ul.tx li{position:relative;padding-left:6px;margin-bottom:3px}
ul.tx li::before{content:"";position:absolute;left:1px;top:1.5px;width:1.5px;height:1.5px;background:var(--blue)}
</style>
</head>
<body>

<!-- 1 cover -->
<section class="slide c1 r1">
  <div class="abs" style="left:0;right:0;top:34px;text-align:center;font-size:28px;color:var(--green)">Traloma</div>
  <div class="abs" style="left:0;right:0;top:102px;height:2px;background:var(--green)"></div>
  <div class="abs" style="left:0;right:0;top:104px;height:42px;background:var(--blue)">
    <div class="abs" style="left:13px;top:9px;font-size:10px;font-weight:700;color:#fff;letter-spacing:.5px">Headline</div>
    <div class="abs" style="left:13px;top:26px;font-size:5.5px;color:#fff">Subtitle</div>
  </div>
</section>

<!-- 2 side panel -->
<section class="slide c2 r1">
  <div class="abs" style="left:0;top:0;width:122px;height:158px;background:var(--blue)">
    <div class="abs" style="left:11px;top:15px;font-size:7px;color:#fff">Title</div>
    <p class="tx w abs" style="left:11px;top:28px;width:102px;font-size:3.8px;line-height:2.35">Lorem ipsum dolor sit amet, consetetur sadipscing elitr, sed diam nonumy eirmod tempor invidunt ut labore et dolore magna aliquyam erat, sed diam voluptua. At vero eos et accusam et justo duo dolores et ea rebum. Stet clita kasd gubergren, no sea takimata sanctus est. Lorem ipsum dolor sit amet. Lorem ipsum dolor sit amet, consetetur sadipscing elitr, sed diam nonumy eirmod tempor invidunt ut labore et dolore magna aliquyam erat, sed diam voluptua. At vero eos et accusam</p>
  </div>
  <div class="ph" role="img" aria-label="Photo placeholder" style="left:122px;top:0;width:160px;height:158px"></div>
</section>

<!-- 3 bottom band -->
<section class="slide c3 r1">
  <div class="ph" role="img" aria-label="Photo placeholder" style="left:0;top:0;width:282px;height:85px"></div>
  <div class="abs" style="left:0;right:0;top:84px;height:2px;background:var(--green)"></div>
  <div class="abs" style="left:0;right:0;top:86px;bottom:0;background:var(--blue)">
    <div class="abs" style="left:11px;top:8px;font-size:7px;color:#fff">Title</div>
    <p class="tx w abs" style="left:11px;top:21px;width:242px">Lorem ipsum dolor sit amet, consetetur sadipscing elitr, sed diam nonumy eirmod tempor invidunt ut labore et dolore magna aliquyam erat, sed diam voluptua. At vero eos et accusam et justo duo dolores et ea rebum. Stet clita kasd gubergren, no sea takimata sanctus est Lorem ipsum dolor sit amet. Lorem ipsum dolor sit amet, consetetur sadipscing elitr, sed diam nonumy eirmod tempor invidunt ut labore et dolore magna aliquyam erat, sed diam voluptua. At vero eos et accusam et</p>
  </div>
</section>

<!-- 4 text + image -->
<section class="slide c4 r1">
  <div class="hd">Headline</div><div class="brand">Traloma</div><div class="rule"></div>
  <p class="tx abs" style="left:10px;top:43px;width:80px;font-size:3.4px;text-align:right">Lorem ipsum dolor sit amet, consetetur sadipscing elitr, sed diam nonumy eirmod tempor invidunt ut labore et dolore magna aliquyam erat, sed diam voluptua. At vero eos et accusam et justo duo dolores et ea rebum. Stet clita kasd gubergren, no sea takimata sanctus est Lorem ipsum dolor sit amet. Lorem ipsum dolor sit amet, consetetur sadipscing elitr, sed diam nonumy eirmod tempor invidunt ut labore et dolore magna aliquyam erat, sed diam voluptua.</p>
  <div class="ph" role="img" aria-label="Photo placeholder" style="left:96px;top:42px;width:174px;height:100px"></div>
</section>

<!-- 5 four columns -->
<section class="slide c1 r2">
  <div class="hd">Headline</div><div class="brand">Traloma</div><div class="rule"></div>
  <div class="ph" role="img" aria-label="Photo placeholder" style="left:18px;top:42px;width:57px;height:74px"></div>
  <div class="ph" role="img" aria-label="Photo placeholder" style="left:81px;top:42px;width:57px;height:74px"></div>
  <div class="ph" role="img" aria-label="Photo placeholder" style="left:143px;top:42px;width:57px;height:74px"></div>
  <div class="ph" role="img" aria-label="Photo placeholder" style="left:206px;top:42px;width:57px;height:74px"></div>
  <div class="bar" style="left:18px;top:116px;width:57px;height:6px;font-size:3.8px">Title</div>
  <div class="bar" style="left:81px;top:116px;width:57px;height:6px;font-size:3.8px">Title</div>
  <div class="bar" style="left:143px;top:116px;width:57px;height:6px;font-size:3.8px">Title</div>
  <div class="bar" style="left:206px;top:116px;width:57px;height:6px;font-size:3.8px">Title</div>
  <ul class="box tx" style="left:18px;top:122px;width:57px;height:28px;font-size:3px"><li>Lorem ipsum dolor sit amet, consetetur sadipscing</li><li>sed diam nonumy eirmod tempor invidunt</li></ul>
  <ul class="box tx" style="left:81px;top:122px;width:57px;height:28px;font-size:3px"><li>Lorem ipsum dolor sit amet, consetetur sadipscing</li><li>sed diam nonumy eirmod tempor invidunt</li></ul>
  <ul class="box tx" style="left:143px;top:122px;width:57px;height:28px;font-size:3px"><li>Lorem ipsum dolor sit amet, consetetur sadipscing</li><li>sed diam nonumy eirmod tempor invidunt</li></ul>
  <ul class="box tx" style="left:206px;top:122px;width:57px;height:28px;font-size:3px"><li>Lorem ipsum dolor sit amet, consetetur sadipscing</li><li>sed diam nonumy eirmod tempor invidunt</li></ul>
</section>

<!-- 6 three columns -->
<section class="slide c2 r2">
  <div class="hd">Headline</div><div class="brand">Traloma</div><div class="rule"></div>
  <div class="ph" role="img" aria-label="Photo placeholder" style="left:19px;top:43px;width:74px;height:61px"></div>
  <div class="ph" role="img" aria-label="Photo placeholder" style="left:107px;top:43px;width:74px;height:61px"></div>
  <div class="ph" role="img" aria-label="Photo placeholder" style="left:195px;top:43px;width:74px;height:61px"></div>
  <div class="bar" style="left:19px;top:104px;width:74px;height:9px;line-height:9px">Title</div>
  <div class="bar" style="left:107px;top:104px;width:74px;height:9px;line-height:9px">Title</div>
  <div class="bar" style="left:195px;top:104px;width:74px;height:9px;line-height:9px">Title</div>
  <p class="tx abs" style="left:21px;top:116px;width:70px;text-align:center">Lorem ipsum dolor sit amet, consetetur sadipscing elitr, sed diam nonumy eirmod tempor invidunt ut labore et dolore magna aliquyam erat</p>
  <p class="tx abs" style="left:109px;top:116px;width:70px;text-align:center">Lorem ipsum dolor sit amet, consetetur sadipscing elitr, sed diam nonumy eirmod tempor invidunt ut labore et dolore magna aliquyam erat</p>
  <p class="tx abs" style="left:197px;top:116px;width:70px;text-align:center">Lorem ipsum dolor sit amet, consetetur sadipscing elitr, sed diam nonumy eirmod tempor invidunt ut labore et dolore magna aliquyam erat</p>
</section>

<!-- 7 image strip -->
<section class="slide c3 r2">
  <div class="hd">Headline</div><div class="brand">Traloma</div><div class="rule"></div>
  <div class="ph" role="img" aria-label="Photo placeholder" style="left:12px;top:46px;width:63px;height:52px"></div>
  <div class="ph" role="img" aria-label="Photo placeholder" style="left:77px;top:46px;width:63px;height:52px"></div>
  <div class="ph" role="img" aria-label="Photo placeholder" style="left:142px;top:46px;width:63px;height:52px"></div>
  <div class="ph" role="img" aria-label="Photo placeholder" style="left:207px;top:46px;width:63px;height:52px"></div>
  <p class="tx abs" style="left:12px;top:103px;width:258px;text-align:justify">Lorem ipsum dolor sit amet, consetetur sadipscing elitr, sed diam nonumy eirmod tempor invidunt ut labore et dolore magna aliquyam erat, sed diam voluptua. At vero eos et accusam et justo duo dolores et ea rebum. Stet clita kasd gubergren, no sea takimata sanctus est Lorem ipsum dolor sit amet. Lorem ipsum dolor sit amet, consetetur sadipscing elitr, sed diam nonumy eirmod tempor invidunt ut labore et dolore magna aliquyam erat, sed diam voluptua. At vero eos et accusam et justo duo dolores et ea rebum. Stet clita kasd gubergren, no sea takimata sanctus est Lorem ipsum.</p>
</section>

<!-- 8 grid with text column -->
<section class="slide c4 r2">
  <div class="hd">Headline</div><div class="brand">Traloma</div><div class="rule"></div>
  <div class="ph" role="img" aria-label="Photo placeholder" style="left:12px;top:38px;width:74px;height:35px"></div>
  <div class="ph" role="img" aria-label="Photo placeholder" style="left:12px;top:76px;width:74px;height:35px"></div>
  <div class="ph" role="img" aria-label="Photo placeholder" style="left:12px;top:114px;width:74px;height:35px"></div>
  <div class="abs" style="left:86px;top:38px;width:109px;height:35px;background:var(--blue);padding:8px 6px"><p class="tx w" style="font-size:3px;text-align:center">Lorem ipsum dolor sit amet, consetetur sadipscing elitr, sed diam nonumy eirmod tempor invidunt ut labore et dolore magna aliquyam erat</p></div>
  <div class="abs" style="left:86px;top:76px;width:109px;height:35px;background:var(--blue);padding:8px 6px"><p class="tx w" style="font-size:3px;text-align:center">Lorem ipsum dolor sit amet, consetetur sadipscing elitr, sed diam nonumy eirmod tempor invidunt ut labore et dolore magna aliquyam erat</p></div>
  <div class="abs" style="left:86px;top:114px;width:109px;height:35px;background:var(--blue);padding:8px 6px"><p class="tx w" style="font-size:3px;text-align:center">Lorem ipsum dolor sit amet, consetetur sadipscing elitr, sed diam nonumy eirmod tempor invidunt ut labore et dolore magna aliquyam erat</p></div>
  <div class="ph" role="img" aria-label="Photo placeholder" style="left:195px;top:38px;width:87px;height:35px"></div>
  <div class="ph" role="img" aria-label="Photo placeholder" style="left:195px;top:76px;width:87px;height:35px"></div>
  <div class="ph" role="img" aria-label="Photo placeholder" style="left:195px;top:114px;width:87px;height:35px"></div>
</section>

<!-- 9 titled rows -->
<section class="slide c1 r3">
  <div class="hd">Headline</div><div class="brand">Traloma</div><div class="rule"></div>
  <div class="bar" style="left:20px;top:38px;width:10px;height:36px;writing-mode:vertical-rl;transform:rotate(180deg);font-size:4px;line-height:10px">Title</div>
  <div class="bar" style="left:20px;top:76px;width:10px;height:36px;writing-mode:vertical-rl;transform:rotate(180deg);font-size:4px;line-height:10px">Title</div>
  <div class="bar" style="left:20px;top:114px;width:10px;height:36px;writing-mode:vertical-rl;transform:rotate(180deg);font-size:4px;line-height:10px">Title</div>
  <div class="ph" role="img" aria-label="Photo placeholder" style="left:30px;top:38px;width:93px;height:36px"></div>
  <div class="ph" role="img" aria-label="Photo placeholder" style="left:30px;top:76px;width:93px;height:36px"></div>
  <div class="ph" role="img" aria-label="Photo placeholder" style="left:30px;top:114px;width:93px;height:36px"></div>
  <p class="tx abs" style="left:127px;top:40px;width:138px;text-align:justify">Lorem ipsum dolor sit amet, consetetur sadipscing elitr, sed diam nonumy eirmod tempor invidunt ut labore et dolore magna aliquyam erat, sed diam voluptua. At vero eos et accusam et justo duo dolores et ea rebum.</p>
  <p class="tx abs" style="left:127px;top:78px;width:138px;text-align:justify">Lorem ipsum dolor sit amet, consetetur sadipscing elitr, sed diam nonumy eirmod tempor invidunt ut labore et dolore magna aliquyam erat, sed diam voluptua. At vero eos et accusam et justo duo dolores et ea rebum.</p>
  <p class="tx abs" style="left:127px;top:116px;width:138px;text-align:justify">Lorem ipsum dolor sit amet, consetetur sadipscing elitr, sed diam nonumy eirmod tempor invidunt ut labore et dolore magna aliquyam erat, sed diam voluptua. At vero eos et accusam et justo duo dolores et ea rebum.</p>
</section>

<!-- 10 bullets + image -->
<section class="slide c2 r3">
  <div class="hd">Headline</div><div class="brand">Traloma</div><div class="rule"></div>
  <ul class="tx abs" style="left:12px;top:46px;width:140px">
    <li style="margin-bottom:6px">Lorem ipsum dolor sit amet, consetetur sadipscing elitr, sed diam nonumy eirmod diam nonumy eirmod</li>
    <li style="margin-bottom:6px">Lorem ipsum dolor sit amet, consetetur sadipscing elitr, sed diam nonumy eirmod diam nonumy eirmod</li>
    <li style="margin-bottom:6px">Lorem ipsum dolor sit amet, consetetur sadipscing elitr, sed diam nonumy eirmod diam nonumy eirmod</li>
    <li style="margin-bottom:6px">Lorem ipsum dolor sit amet, consetetur sadipscing elitr, sed diam nonumy eirmod diam nonumy eirmod</li>
    <li>Lorem ipsum dolor sit amet, consetetur sadipscing elitr, sed diam nonumy eirmod diam nonumy eirmod</li>
  </ul>
  <div class="ph" role="img" aria-label="Photo placeholder" style="left:155px;top:40px;width:115px;height:104px"></div>
</section>

<!-- 11 two title boxes -->
<section class="slide c3 r3">
  <div class="hd" style="top:17px">Headline</div><div class="brand">Traloma</div><div class="rule"></div>
  <div class="bar" style="left:13px;top:42px;width:37px;height:52px;line-height:52px;font-size:5.5px">Title</div>
  <div class="bar" style="left:13px;top:96px;width:37px;height:52px;line-height:52px;font-size:5.5px">Title</div>
  <ul class="box tx" style="left:50px;top:42px;width:196px;height:52px;padding:5px 4px"><li style="margin-bottom:4px">Lorem ipsum dolor sit amet, consetetur sadipscing elitr, sed diam nonumy eirmod tempor invidunt ut labore et dolore magna aliquyam erat, sed diam voluptua. At vero eos et accusam et justo duo dolores et ea rebum.</li><li>Lorem ipsum dolor sit amet, consetetur sadipscing elitr, sed diam nonumy eirmod tempor invidunt ut labore et dolore magna aliquyam erat, sed diam voluptua. At vero eos et accusam et justo duo dolores et ea rebum.</li></ul>
  <ul class="box tx" style="left:50px;top:96px;width:196px;height:52px;padding:5px 4px"><li style="margin-bottom:4px">Lorem ipsum dolor sit amet, consetetur sadipscing elitr, sed diam nonumy eirmod tempor invidunt ut labore et dolore magna aliquyam erat, sed diam voluptua. At vero eos et accusam et justo duo dolores et ea rebum.</li><li>Lorem ipsum dolor sit amet, consetetur sadipscing elitr, sed diam nonumy eirmod tempor invidunt ut labore et dolore magna aliquyam erat, sed diam voluptua. At vero eos et accusam et justo duo dolores et ea rebum.</li></ul>
</section>

<!-- 12 title rows -->
<section class="slide c4 r3">
  <div class="hd" style="top:17px">Headline</div><div class="brand">Traloma</div><div class="rule"></div>
  <div class="bar" style="left:10px;top:45px;width:71px;height:25px;line-height:25px">Title</div>
  <div class="bar" style="left:10px;top:73px;width:71px;height:25px;line-height:25px">Title</div>
  <div class="bar" style="left:10px;top:101px;width:71px;height:25px;line-height:25px">Title</div>
  <div class="bar" style="left:10px;top:129px;width:71px;height:25px;line-height:25px">Title</div>
  <p class="tx abs" style="left:86px;top:46px;width:180px">Lorem ipsum dolor sit amet, consetetur sadipscing elitr, sed diam nonumy eirmod tempor invidunt ut labore et dolore magna aliquyam erat, sed diam voluptua. At vero eos et accusam et justo duo dolores et ea rebum.</p>
  <p class="tx abs" style="left:86px;top:74px;width:180px">Lorem ipsum dolor sit amet, consetetur sadipscing elitr, sed diam nonumy eirmod tempor invidunt ut labore et dolore magna aliquyam erat, sed diam voluptua. At vero eos et accusam et justo duo dolores et ea rebum.</p>
  <p class="tx abs" style="left:86px;top:102px;width:180px">Lorem ipsum dolor sit amet, consetetur sadipscing elitr, sed diam nonumy eirmod tempor invidunt ut labore et dolore magna aliquyam erat, sed diam voluptua. At vero eos et accusam et justo duo dolores et ea rebum.</p>
  <p class="tx abs" style="left:86px;top:130px;width:180px">Lorem ipsum dolor sit amet, consetetur sadipscing elitr, sed diam nonumy eirmod tempor invidunt ut labore et dolore magna aliquyam erat, sed diam voluptua. At vero eos et accusam et justo duo dolores et ea rebum.</p>
</section>

<!-- 13 tabbed text boxes -->
<section class="slide c1 r4">
  <div class="hd">Headline</div><div class="brand">Traloma</div><div class="rule"></div>
  <div class="abs" style="left:12px;top:46px;width:56px;height:2px;background:var(--blue)"></div>
  <p class="box tx" style="left:12px;top:48px;width:248px;height:21px">Lorem ipsum dolor sit amet, consetetur sadipscing elitr, sed diam nonumy eirmod tempor invidunt ut labore et dolore magna aliquyam erat, sed diam voluptua. At vero eos et accusam et justo duo dolores et ea rebum.</p>
  <div class="abs" style="left:12px;top:71px;width:56px;height:2px;background:var(--blue)"></div>
  <p class="box tx" style="left:12px;top:73px;width:248px;height:21px">Lorem ipsum dolor sit amet, consetetur sadipscing elitr, sed diam nonumy eirmod tempor invidunt ut labore et dolore magna aliquyam erat, sed diam voluptua. At vero eos et accusam et justo duo dolores et ea rebum.</p>
  <div class="abs" style="left:12px;top:96px;width:56px;height:2px;background:var(--blue)"></div>
  <p class="box tx" style="left:12px;top:98px;width:248px;height:21px">Lorem ipsum dolor sit amet, consetetur sadipscing elitr, sed diam nonumy eirmod tempor invidunt ut labore et dolore magna aliquyam erat, sed diam voluptua. At vero eos et accusam et justo duo dolores et ea rebum.</p>
  <div class="abs" style="left:12px;top:121px;width:56px;height:2px;background:var(--blue)"></div>
  <p class="box tx" style="left:12px;top:123px;width:248px;height:21px">Lorem ipsum dolor sit amet, consetetur sadipscing elitr, sed diam nonumy eirmod tempor invidunt ut labore et dolore magna aliquyam erat, sed diam voluptua. At vero eos et accusam et justo duo dolores et ea rebum.</p>
</section>

<!-- 14 tabbed columns -->
<section class="slide c2 r4">
  <div class="hd">Headline</div><div class="brand">Traloma</div><div class="rule"></div>
  <div class="bar" style="left:14px;top:50px;width:51px;height:7px;line-height:7px;text-align:left;padding-left:3px;font-size:4px">Title</div>
  <div class="bar" style="left:101px;top:50px;width:51px;height:7px;line-height:7px;text-align:left;padding-left:3px;font-size:4px">Title</div>
  <div class="bar" style="left:188px;top:50px;width:51px;height:7px;line-height:7px;text-align:left;padding-left:3px;font-size:4px">Title</div>
  <ul class="box tx" style="left:14px;top:57px;width:81px;height:72px;padding:6px 3px"><li style="margin-bottom:5px">Lorem ipsum dolor sit amet, consetetur sadipscing elitr, sed diam nonumy eirmod tempor</li><li style="margin-bottom:5px">Lorem ipsum dolor sit amet, consetetur sadipscing elitr, sed diam nonumy eirmod tempor</li><li>Lorem ipsum dolor sit amet, consetetur sadipscing elitr, sed diam nonumy eirmod tempor</li></ul>
  <ul class="box tx" style="left:101px;top:57px;width:81px;height:72px;padding:6px 3px"><li style="margin-bottom:5px">Lorem ipsum dolor sit amet, consetetur sadipscing elitr, sed diam nonumy eirmod tempor</li><li style="margin-bottom:5px">Lorem ipsum dolor sit amet, consetetur sadipscing elitr, sed diam nonumy eirmod tempor</li><li>Lorem ipsum dolor sit amet, consetetur sadipscing elitr, sed diam nonumy eirmod tempor</li></ul>
  <ul class="box tx" style="left:188px;top:57px;width:81px;height:72px;padding:6px 3px"><li style="margin-bottom:5px">Lorem ipsum dolor sit amet, consetetur sadipscing elitr, sed diam nonumy eirmod tempor</li><li style="margin-bottom:5px">Lorem ipsum dolor sit amet, consetetur sadipscing elitr, sed diam nonumy eirmod tempor</li><li>Lorem ipsum dolor sit amet, consetetur sadipscing elitr, sed diam nonumy eirmod tempor</li></ul>
</section>

<!-- 15 bullet paragraphs -->
<section class="slide c3 r4">
  <div class="hd">Headline</div><div class="brand">Traloma</div><div class="rule"></div>
  <div class="abs" style="left:18px;top:46px;width:250px">
    <p style="font-size:6px;line-height:1.4;color:var(--text)"><span style="color:var(--blue)">■</span> Lorem ipsum dolor sit amet, consetetur sadipscing elitr, sed diam nonumy eirmod tempor invidunt ut labore et dolore magna aliquyam erat, sed diam voluptua.</p>
    <ul class="tx" style="font-size:3px;margin:3px 0 0 8px"><li style="margin-bottom:1px">Lorem ipsum dolor sit amet, consetetur sadipscing elitr, sed diam nonumy eirmod tempor invidunt ut labore et dolore magna aliquyam erat, sed diam voluptua. Lorem ipsum dolor sit amet, consetetur sadipscing elitr, sed diam.</li><li>Lorem ipsum dolor sit amet, consetetur sadipscing elitr, sed diam nonumy eirmod tempor invidunt ut labore et dolore magna aliquyam erat, sed diam voluptua. Lorem ipsum dolor sit amet.</li></ul>
    <p style="font-size:6px;line-height:1.4;color:var(--text);margin-top:8px"><span style="color:var(--blue)">■</span> Lorem ipsum dolor sit amet, consetetur sadipscing elitr, sed diam nonumy eirmod tempor invidunt ut labore et dolore magna aliquyam erat, sed diam voluptua.</p>
    <ul class="tx" style="font-size:3px;margin:3px 0 0 8px"><li style="margin-bottom:1px">Lorem ipsum dolor sit amet, consetetur sadipscing elitr, sed diam nonumy eirmod tempor invidunt ut labore et dolore magna aliquyam erat, sed diam voluptua. Lorem ipsum dolor sit amet, consetetur sadipscing elitr, sed diam.</li><li>Lorem ipsum dolor sit amet, consetetur sadipscing elitr, sed diam nonumy eirmod tempor invidunt ut labore et dolore magna aliquyam erat, sed diam voluptua. Lorem ipsum dolor sit amet.</li></ul>
  </div>
</section>

<!-- 16 chevron columns -->
<section class="slide c4 r4">
  <div class="hd">Headline</div><div class="brand">Traloma</div><div class="rule"></div>
  <svg class="abs" style="left:16px;top:46px" width="250" height="14" viewBox="0 0 250 14" aria-hidden="true">
    <polygon points="0,0 77,0 83,7 77,14 0,14 5,7" fill="#2d8be3"/>
    <polygon points="83,0 160,0 166,7 160,14 83,14 88,7" fill="#2d8be3"/>
    <polygon points="166,0 243,0 249,7 243,14 166,14 171,7" fill="#2d8be3"/>
  </svg>
  <div class="abs" style="left:16px;top:49px;width:83px;text-align:center;font-size:6.5px;font-weight:700;color:#fff">Title</div>
  <div class="abs" style="left:99px;top:49px;width:83px;text-align:center;font-size:6.5px;font-weight:700;color:#fff">Title</div>
  <div class="abs" style="left:182px;top:49px;width:83px;text-align:center;font-size:6.5px;font-weight:700;color:#fff">Title</div>
  <ul class="tx abs" style="left:22px;top:64px;width:76px;font-size:3.4px"><li>Lorem ipsum dolor sit amet, consetetur sadipscing elitr, sed diam nonumy eirmod.</li><li>Lorem ipsum dolor sit amet, consetetur sadipscing elitr, sed diam nonumy eirmod.</li><li>Lorem ipsum dolor sit amet, consetetur sadipscing elitr, sed diam nonumy eirmod.</li></ul>
  <ul class="tx abs" style="left:105px;top:64px;width:76px;font-size:3.4px"><li>Lorem ipsum dolor sit amet, consetetur sadipscing elitr, sed diam nonumy eirmod.</li><li>Lorem ipsum dolor sit amet, consetetur sadipscing elitr, sed diam nonumy eirmod.</li><li>Lorem ipsum dolor sit amet, consetetur sadipscing elitr, sed diam nonumy eirmod.</li></ul>
  <ul class="tx abs" style="left:188px;top:64px;width:76px;font-size:3.4px"><li>Lorem ipsum dolor sit amet, consetetur sadipscing elitr, sed diam nonumy eirmod.</li><li>Lorem ipsum dolor sit amet, consetetur sadipscing elitr, sed diam nonumy eirmod.</li><li>Lorem ipsum dolor sit amet, consetetur sadipscing elitr, sed diam nonumy eirmod.</li></ul>
  <div class="bar" style="left:19px;top:128px;width:79px;height:14px;font-size:3.5px;font-weight:400;padding-top:2px">Lorem ipsum dolor sit amet, consetetur sadipscing elitr</div>
  <div class="bar" style="left:102px;top:128px;width:79px;height:14px;font-size:3.5px;font-weight:400;padding-top:2px">Lorem ipsum dolor sit amet, consetetur sadipscing elitr</div>
  <div class="bar" style="left:185px;top:128px;width:79px;height:14px;font-size:3.5px;font-weight:400;padding-top:2px">Lorem ipsum dolor sit amet, consetetur sadipscing elitr</div>
</section>

<!-- 17 bar + line charts -->
<section class="slide c1 r5">
  <div class="hd">Headline</div><div class="brand">Traloma</div><div class="rule"></div>
  <div class="bar" style="left:24px;top:49px;width:104px;height:7px;line-height:7px;font-size:4.5px">Title</div>
  <div class="bar" style="left:150px;top:49px;width:105px;height:7px;line-height:7px;font-size:4.5px">Title</div>
  <svg class="abs" style="left:22px;top:58px" width="110" height="70" viewBox="0 0 110 70" role="img" aria-label="Grouped bar chart">
    <g stroke="#e2e2e2" stroke-width=".4"><line x1="10" y1="10" x2="108" y2="10"/><line x1="10" y1="20" x2="108" y2="20"/><line x1="10" y1="30" x2="108" y2="30"/><line x1="10" y1="40" x2="108" y2="40"/><line x1="10" y1="50" x2="108" y2="50"/><line x1="10" y1="60" x2="108" y2="60"/></g>
    <g fill="#7cc143"><rect x="14" y="51" width="3" height="9"/><rect x="26" y="48" width="3" height="12"/><rect x="38" y="46" width="3" height="14"/><rect x="50" y="43" width="3" height="17"/><rect x="62" y="41" width="3" height="19"/><rect x="74" y="38" width="3" height="22"/><rect x="86" y="36" width="3" height="24"/><rect x="98" y="45" width="3" height="15"/></g>
    <g fill="#2d8be3"><rect x="17" y="47" width="3" height="13"/><rect x="29" y="43" width="3" height="17"/><rect x="41" y="40" width="3" height="20"/><rect x="53" y="36" width="3" height="24"/><rect x="65" y="33" width="3" height="27"/><rect x="77" y="22" width="3" height="38"/><rect x="89" y="28" width="3" height="32"/><rect x="101" y="42" width="3" height="18"/></g>
    <g font-size="3" fill="#777"><text x="2" y="11">70</text><text x="2" y="21">60</text><text x="2" y="31">50</text><text x="2" y="41">40</text><text x="2" y="51">20</text><text x="2" y="61">0</text><text x="13" y="65">Text</text><text x="37" y="65">Text</text><text x="61" y="65">Text</text><text x="85" y="65">Text</text></g>
  </svg>
  <svg class="abs" style="left:148px;top:58px" width="110" height="70" viewBox="0 0 110 70" role="img" aria-label="Line chart">
    <g stroke="#e2e2e2" stroke-width=".4"><line x1="10" y1="10" x2="108" y2="10"/><line x1="10" y1="20" x2="108" y2="20"/><line x1="10" y1="30" x2="108" y2="30"/><line x1="10" y1="40" x2="108" y2="40"/><line x1="10" y1="50" x2="108" y2="50"/><line x1="10" y1="60" x2="108" y2="60"/></g>
    <polyline points="14,30 26,34 38,32 50,24 62,34 74,30 86,22 98,30" fill="none" stroke="#2d8be3" stroke-width=".9"/>
    <polyline points="14,36 26,42 38,44 50,34 62,28 74,40 86,26 98,36" fill="none" stroke="#7cc143" stroke-width=".9"/>
    <g font-size="3" fill="#777"><text x="2" y="11">70</text><text x="2" y="31">50</text><text x="2" y="51">20</text><text x="13" y="65">Text</text><text x="37" y="65">Text</text><text x="61" y="65">Text</text><text x="85" y="65">Text</text></g>
  </svg>
  <p class="tx abs" style="left:28px;top:136px;width:100px;text-align:center">Lorem ipsum dolor sit amet, consetetur sadipscing elitr, sed diam nonumy eirmod tempor invidunt ut</p>
  <p class="tx abs" style="left:154px;top:136px;width:100px;text-align:center">Lorem ipsum dolor sit amet, consetetur sadipscing elitr, sed diam nonumy eirmod tempor invidunt ut</p>
</section>

<!-- 18 four mini charts -->
<section class="slide c2 r5">
  <div class="hd">Headline</div><div class="brand">Traloma</div><div class="rule"></div>
  <div class="bar" style="left:14px;top:45px;width:86px;height:5px;font-size:3px;line-height:5px">Title</div>
  <div class="bar" style="left:108px;top:45px;width:86px;height:5px;font-size:3px;line-height:5px">Title</div>
  <div class="bar" style="left:14px;top:103px;width:86px;height:5px;font-size:3px;line-height:5px">Title</div>
  <div class="bar" style="left:108px;top:103px;width:86px;height:5px;font-size:3px;line-height:5px">Title</div>
  <svg class="abs" style="left:14px;top:51px" width="180" height="105" viewBox="0 0 180 105" role="img" aria-label="Four small charts">
    <g stroke="#e2e2e2" stroke-width=".4">
      <line x1="6" y1="8" x2="86" y2="8"/><line x1="6" y1="20" x2="86" y2="20"/><line x1="6" y1="32" x2="86" y2="32"/><line x1="6" y1="44" x2="86" y2="44"/>
      <line x1="100" y1="8" x2="180" y2="8"/><line x1="100" y1="20" x2="180" y2="20"/><line x1="100" y1="32" x2="180" y2="32"/><line x1="100" y1="44" x2="180" y2="44"/>
      <line x1="6" y1="66" x2="86" y2="66"/><line x1="6" y1="80" x2="86" y2="80"/><line x1="6" y1="94" x2="86" y2="94"/>
      <line x1="100" y1="66" x2="180" y2="66"/><line x1="100" y1="80" x2="180" y2="80"/><line x1="100" y1="94" x2="180" y2="94"/>
    </g>
    <polyline points="8,38 18,32 28,14 38,20 48,22 58,22 68,24 78,26 86,22" fill="none" stroke="#2d8be3" stroke-width=".9"/>
    <polyline points="102,34 112,32 122,34 132,30 142,32 152,34 162,32 172,30 180,32" fill="none" stroke="#2d8be3" stroke-width=".9"/>
    <g fill="#2d8be3">
      <rect x="8" y="78" width="4" height="16"/><rect x="14" y="74" width="4" height="20"/><rect x="20" y="76" width="4" height="18"/><rect x="26" y="72" width="4" height="22"/><rect x="32" y="78" width="4" height="16"/><rect x="38" y="74" width="4" height="20"/><rect x="44" y="80" width="4" height="14"/><rect x="50" y="75" width="4" height="19"/><rect x="56" y="77" width="4" height="17"/><rect x="62" y="73" width="4" height="21"/><rect x="68" y="79" width="4" height="15"/><rect x="74" y="74" width="4" height="20"/><rect x="80" y="77" width="4" height="17"/>
      <rect x="102" y="80" width="4" height="14"/><rect x="108" y="76" width="4" height="18"/><rect x="114" y="78" width="4" height="16"/><rect x="120" y="74" width="4" height="20"/><rect x="126" y="80" width="4" height="14"/><rect x="132" y="77" width="4" height="17"/><rect x="138" y="75" width="4" height="19"/><rect x="144" y="73" width="4" height="21"/><rect x="150" y="79" width="4" height="15"/><rect x="156" y="76" width="4" height="18"/><rect x="162" y="74" width="4" height="20"/><rect x="168" y="78" width="4" height="16"/><rect x="174" y="75" width="4" height="19"/>
    </g>
  </svg>
  <ul class="tx abs" style="left:203px;top:44px;width:70px;font-size:3.8px"><li style="margin-bottom:8px">Lorem ipsum dolor sit amet, consetetur sadipscing elitr, sed diam nonumy eirmod tempor invidunt ut labore et dolore</li><li>Lorem ipsum dolor sit amet, consetetur sadipscing elitr, sed diam nonumy eirmod tempor invidunt ut labore et dolore</li></ul>
</section>

<!-- 19 donut -->
<section class="slide c3 r5">
  <div class="hd">Headline</div><div class="brand">Traloma</div><div class="rule"></div>
  <svg class="abs" style="left:40px;top:50px" width="90" height="90" viewBox="0 0 90 90" role="img" aria-label="Donut chart: 59, 23, 10 and 9 percent">
    <g fill="none" stroke-width="14" transform="rotate(-90 45 45)">
      <circle cx="45" cy="45" r="33" stroke="#2d8be3" stroke-dasharray="122.3 207.3"/>
      <circle cx="45" cy="45" r="33" stroke="#7cc143" stroke-dasharray="47.7 207.3" stroke-dashoffset="-122.3"/>
      <circle cx="45" cy="45" r="33" stroke="#86c9a8" stroke-dasharray="20.7 207.3" stroke-dashoffset="-170"/>
      <circle cx="45" cy="45" r="33" stroke="#7fa7c9" stroke-dasharray="16.6 207.3" stroke-dashoffset="-190.7"/>
    </g>
    <g font-size="3.5" fill="#fff" text-anchor="middle"><text x="70" y="60">Text</text><text x="70" y="64">59%</text><text x="18" y="59">Text</text><text x="18" y="63">23%</text><text x="19" y="35">Text</text><text x="19" y="39">10%</text><text x="34" y="17">Text</text><text x="34" y="21">9%</text></g>
  </svg>
  <div class="bar" style="left:152px;top:62px;width:95px;height:8px;line-height:8px">Title</div>
  <ul class="tx abs" style="left:152px;top:74px;width:95px;font-size:3.9px"><li style="margin-bottom:6px">Lorem ipsum dolor sit amet, consetetur sadipscing elitr, sed diam nonumy eirmod tempor invidunt ut labore et dolore</li><li>Lorem ipsum dolor sit amet, consetetur sadipscing elitr, sed diam nonumy eirmod tempor invidunt ut labore et dolore</li></ul>
</section>

<!-- 20 horizontal bars -->
<section class="slide c4 r5">
  <div class="hd">Headline</div><div class="brand">Traloma</div><div class="rule"></div>
  <svg class="abs" style="left:12px;top:52px" width="150" height="90" viewBox="0 0 150 90" role="img" aria-label="Horizontal bar chart">
    <line x1="17" y1="0" x2="17" y2="90" stroke="#ccc" stroke-width=".4"/>
    <g fill="#2d8be3">
      <rect x="17" y="2" width="125" height="5"/><rect x="17" y="11" width="116" height="5"/><rect x="17" y="20" width="116" height="5"/><rect x="17" y="29" width="104" height="5"/><rect x="17" y="38" width="96" height="5"/><rect x="17" y="47" width="88" height="5"/><rect x="17" y="56" width="84" height="5"/><rect x="17" y="65" width="68" height="5"/><rect x="17" y="74" width="56" height="5"/><rect x="17" y="83" width="52" height="5"/>
    </g>
    <g font-size="3.5" fill="#555">
      <text x="2" y="6">Text</text><text x="2" y="15">Text</text><text x="2" y="24">Text</text><text x="2" y="33">Text</text><text x="2" y="42">Text</text><text x="2" y="51">Text</text><text x="2" y="60">Text</text><text x="2" y="69">Text</text><text x="2" y="78">Text</text><text x="2" y="87">Text</text>
      <text x="144" y="6">31</text><text x="135" y="15">29</text><text x="135" y="24">29</text><text x="123" y="33">26</text><text x="115" y="42">24</text><text x="107" y="51">22</text><text x="103" y="60">21</text><text x="87" y="69">17</text><text x="75" y="78">14</text><text x="71" y="87">13</text>
    </g>
  </svg>
  <ul class="tx abs" style="left:176px;top:64px;width:95px;font-size:3.9px"><li style="margin-bottom:7px">Lorem ipsum dolor sit amet, consetetur sadipscing elitr, sed diam nonumy eirmod tempor invidunt ut labore et dolore</li><li>Lorem ipsum dolor sit amet, consetetur sadipscing elitr, sed diam nonumy eirmod tempor invidunt ut labore et dolore</li></ul>
</section>

<!-- 21 bars with trend line -->
<section class="slide c1 r6">
  <div class="hd">Headline</div><div class="brand">Traloma</div><div class="rule"></div>
  <p class="tx abs" style="left:12px;top:67px;width:62px;font-size:4.4px">Lorem ipsum dolor sit amet, consetetur sadipscing elitr, sed diam nonumy eirmod tempor invidunt ut labore et dolore magna aliquyam erat, sed diam voluptua. At vero eos et accusam et justo duo dolores et ea rebum.</p>
  <svg class="abs" style="left:82px;top:42px" width="195" height="110" viewBox="0 0 195 110" role="img" aria-label="Bar chart with rising trend line">
    <g fill="#2d8be3">
      <rect x="5" y="74" width="9" height="26"/><rect x="18" y="72" width="9" height="28"/><rect x="31" y="66" width="9" height="34"/><rect x="44" y="58" width="9" height="42"/><rect x="57" y="56" width="9" height="44"/><rect x="70" y="52" width="9" height="48"/><rect x="83" y="48" width="9" height="52"/><rect x="96" y="42" width="9" height="58"/><rect x="109" y="42" width="9" height="58"/><rect x="122" y="38" width="9" height="62"/><rect x="135" y="36" width="9" height="64"/><rect x="148" y="32" width="9" height="68"/>
    </g>
    <polyline points="9.5,56 22.5,54 35.5,48 48.5,42 61.5,40 74.5,36 87.5,32 100.5,28 113.5,28 126.5,24 139.5,20 152.5,20" fill="none" stroke="#7cc143" stroke-width=".9"/>
    <g fill="#7cc143"><circle cx="9.5" cy="56" r="1"/><circle cx="22.5" cy="54" r="1"/><circle cx="35.5" cy="48" r="1"/><circle cx="48.5" cy="42" r="1"/><circle cx="61.5" cy="40" r="1"/><circle cx="74.5" cy="36" r="1"/><circle cx="87.5" cy="32" r="1"/><circle cx="100.5" cy="28" r="1"/><circle cx="113.5" cy="28" r="1"/><circle cx="126.5" cy="24" r="1"/><circle cx="139.5" cy="20" r="1"/><circle cx="152.5" cy="20" r="1"/></g>
    <g font-size="3.8" fill="#7cc143" text-anchor="middle"><text x="9.5" y="53">16</text><text x="22.5" y="51">17</text><text x="35.5" y="45">20</text><text x="48.5" y="39">24</text><text x="61.5" y="37">25</text><text x="74.5" y="33">27</text><text x="87.5" y="29">29</text><text x="100.5" y="25">32</text><text x="113.5" y="25">32</text><text x="126.5" y="21">34</text><text x="139.5" y="17">36</text><text x="152.5" y="17">36</text><text x="168" y="22">Text</text></g>
    <g font-size="3.8" fill="#fff" text-anchor="middle"><text x="9.5" y="97">13</text><text x="22.5" y="97">14</text><text x="35.5" y="97">17</text><text x="48.5" y="88">21</text><text x="61.5" y="88">22</text><text x="74.5" y="84">24</text><text x="87.5" y="80">26</text><text x="100.5" y="72">29</text><text x="113.5" y="72">29</text><text x="126.5" y="68">31</text><text x="139.5" y="66">32</text><text x="152.5" y="62">34</text></g>
    <text x="168" y="61" font-size="3.8" fill="#2d8be3" text-anchor="middle">Text</text>
    <g font-size="3.6" fill="#555" text-anchor="middle"><text x="9.5" y="107">Text</text><text x="22.5" y="107">Text</text><text x="35.5" y="107">Text</text><text x="48.5" y="107">Text</text><text x="61.5" y="107">Text</text><text x="74.5" y="107">Text</text><text x="87.5" y="107">Text</text><text x="100.5" y="107">Text</text><text x="113.5" y="107">Text</text><text x="126.5" y="107">Text</text><text x="139.5" y="107">Text</text><text x="152.5" y="107">Text</text></g>
  </svg>
</section>

</body>
</html>
```